UK landscaping company needs website

We, Brindle Landscapes need a website design for a company based in Surrey, UK. The design should be bold and playful. We have three main areas of work driveways, paving and fencing. It shouldn't be too heavy in text and concentrate on the pictures from previous jobs we've completed. You may use stock images for the design, these can be changed if you are successful. Please don’t just copy the flyer it is just there to provide content.
We have a logo design which we would also like editing slightly.
Here are some of my local competitors
https://www.vexmoorlandscapes.co.uk/

https://www.twinreedgardendesign.com/

https://quarnelllandscapes.co.uk/

Industry/Entity Type

Landscaping

Coding

Coded - Design and coding required

Number of Pages Required

3 page

Font styles to use
Sans Serif

Requirements
Must have
• Pictures of my previous jobs.
Must be mobile friendly
Easy to navigate
Nice to have
• Try to use different colours. It would be good to have some designs that aren’t just black and green.
I’d like some curves in the design.
Should not have
• We install hard landscaping. Think more building/construction and less plants and cutting grass.

```html
<!DOCTYPE html>
<html lang="en">
<head>
<meta charset="utf-8">
<title>Brindle Landscapes</title>
<link href="https://fonts.googleapis.com/css2?family=Lato:wght@400;700;900&display=swap" rel="stylesheet">
<style>
:root{
  --green:#6bbb3a;
  --green-dark:#4d9a22;
  --orange:#f48120;
  --ink:#111111;
  --text:#555555;
  --mist:#f4f4f4;
  --white:#ffffff;
  --line:#c9c9c9;
}
*{margin:0;padding:0;box-sizing:border-box}
html,body{width:1200px;height:4992px;overflow:hidden;background:var(--white);font-family:"Lato",sans-serif;color:var(--text)}
.page{position:relative;width:1200px;height:4992px;overflow:hidden}
.abs{position:absolute}
.center{left:0;width:1200px;text-align:center}

/* header */
.hero-photo{left:0;top:0;width:1200px;height:900px;background:linear-gradient(180deg,#7b6a5e 0%,#8e8a82 35%,#b9b9b4 55%,#4f6a34 80%,#3e5a28 100%)}
.header-bar{left:0;top:0;width:1200px;height:122px;background:rgba(20,20,20,.72)}
.brand{left:112px;top:18px;color:var(--white);font-weight:900;font-size:40px;line-height:1;letter-spacing:1px}
.brand small{display:block;font-size:40px}
.top-contact{right:110px;top:22px;color:var(--white);font-size:17px;display:flex;align-items:center;gap:12px}
.top-contact svg{width:16px;height:16px;fill:var(--orange)}
.nav{left:576px;top:68px;display:flex;gap:0;font-size:17px;font-weight:700;color:var(--white)}
.nav a{color:var(--white);text-decoration:none;position:absolute;white-space:nowrap}
.nav a.active{color:var(--orange)}
.nav a.active::after{content:"";position:absolute;left:0;right:0;bottom:-10px;height:3px;background:var(--orange)}
.hero-title{left:107px;top:228px;font-weight:900;font-size:70px;line-height:88px;color:var(--white);text-shadow:0 2px 6px rgba(0,0,0,.35)}
.hero-title span{color:var(--green)}
.hero-arrow{top:340px;width:30px;height:40px;stroke:var(--white);stroke-width:4;fill:none}

/* headings */
.kicker{color:var(--green);font-size:32px;font-weight:400}
.heading{color:var(--ink);font-size:46px;font-weight:900;letter-spacing:-.5px}
.heading.light{color:var(--white)}
.swoosh{width:180px;height:44px;left:510px}

.copy{font-size:16.5px;line-height:29px;color:var(--text)}
.call{font-size:21px;color:#333}
.phone-big{font-size:30px;font-weight:700;color:var(--orange);display:flex;justify-content:center;align-items:center;gap:14px}
.phone-big svg{width:26px;height:26px;fill:var(--orange)}

/* services */
.svc{width:330px;text-align:center}
.svc-ring{width:318px;height:318px;border-radius:50%;border:13px solid var(--green);margin:0 auto;overflow:hidden;background:var(--white);padding:0}
.svc-ring.orange{border-color:var(--orange)}
.svc-photo{width:100%;height:100%;border-radius:50%}
.svc-stem{width:18px;height:68px;background:var(--ink);margin:12px auto 0}
.svc-title{font-size:25px;font-weight:900;color:var(--ink);margin-top:66px}
.svc-text{font-size:16.5px;line-height:28px;margin-top:10px}
.svc-more{font-size:17px;font-weight:700;color:var(--green);margin-top:14px;display:block}
.svc-more.orange{color:var(--orange)}
.side-arrow{width:26px;height:40px;stroke:#777;stroke-width:4;fill:none}

/* gallery */
.tile{background:var(--white);border:1px solid #e2e2e2;box-shadow:0 1px 4px rgba(0,0,0,.12);padding:8px}
.tile-photo{width:100%}
.btn{background:var(--orange);color:var(--white);font-size:20px;font-weight:700;border-radius:34px;display:flex;align-items:center;justify-content:center}

/* testimonials */
.quote-mark{left:920px;top:3190px;font-size:470px;line-height:1;font-weight:900;color:var(--white)}
.avatar{left:531px;top:3537px;width:136px;height:136px;border-radius:50%;border:6px solid var(--white);background:linear-gradient(160deg,#dfe6ea,#9aa8b0)}
.review{left:250px;top:3690px;width:700px;text-align:center;font-style:italic;font-size:17px;line-height:29px;color:var(--white)}
.reviewer{top:3796px;font-size:19px;font-weight:700;color:var(--white)}
.round-btn{width:48px;height:48px;border-radius:50%;background:var(--white);display:flex;align-items:center;justify-content:center}
.round-btn svg{width:18px;height:18px;stroke:#555;stroke-width:2.5;fill:none}

/* contact form */
.field{border:1px solid var(--line);background:var(--white);font-size:17px;color:#666;padding:14px 26px}

/* footer */
.foot-brand{top:4700px;font-size:80px;font-weight:900;color:var(--white);line-height:1}
.foot-contact{top:4838px;font-size:18px;color:var(--white);display:flex;justify-content:center;align-items:center;gap:22px}
.foot-contact svg{width:16px;height:16px;fill:var(--orange)}
.socials{top:4888px;display:flex;justify-content:center;gap:10px}
.socials span{width:40px;height:40px;border-radius:50%;border:2px solid var(--white)}
.copyright{top:4946px;font-size:15px;color:var(--white)}
</style>
</head>
<body>
<div class="page">

  <!-- hero -->
  <div class="abs hero-photo" role="img" aria-label="Photo of a finished garden with grey porcelain paving, lawn and a timber trellis fence"></div>
  <svg class="abs" style="left:0;top:540px" width="1200" height="380" viewBox="0 540 1200 380">
    <path d="M0,880 C140,660 460,560 1200,640 L1200,920 L0,920 Z" fill="var(--green)"/>
    <path d="M0,900 C150,690 480,588 1200,664 L1200,920 L0,920 Z" fill="var(--white)"/>
  </svg>

  <div class="abs header-bar"></div>
  <div class="abs brand">BRINDLE<br><small style="font-size:17px;letter-spacing:3px;margin-top:4px;margin-left:118px;font-weight:900">LANDSCAPES</small></div>
  <div class="abs top-contact">
    <svg viewBox="0 0 24 24"><path d="M6.6 10.8a15.2 15.2 0 0 0 6.6 6.6l2.2-2.2a1 1 0 0 1 1-.25 11.4 11.4 0 0 0 3.6.57 1 1 0 0 1 1 1V20a1 1 0 0 1-1 1A17 17 0 0 1 3 4a1 1 0 0 1 1-1h3.5a1 1 0 0 1 1 1c0 1.25.2 2.45.57 3.57a1 1 0 0 1-.25 1z"/></svg>
    <span>07700 900 418</span><span>|</span>
    <svg viewBox="0 0 24 24"><path d="M2 5h20v14H2z M2 5l10 8 10-8" /></svg>
    <span>info@brindle-landscapes.com</span>
  </div>
  <nav class="abs nav" style="left:0;top:68px;width:1200px;height:30px">
    <a class="active" style="left:576px">HOME</a>
    <a style="left:663px">ABOUT US</a>
    <a style="left:779px">SERVICES</a>
    <a style="left:891px">PROJECTS</a>
    <a style="left:1008px">CONTACT</a>
  </nav>
  <h1 class="abs hero-title"><span>D</span>RIVEWAYS<br><span>P</span>AVING<br><span>F</span>ENCING</h1>
  <svg class="abs hero-arrow" style="left:40px" viewBox="0 0 30 40"><path d="M22 4 L8 20 L22 36"/></svg>
  <svg class="abs hero-arrow" style="left:1130px" viewBox="0 0 30 40"><path d="M8 4 L22 20 L8 36"/></svg>

  <!-- about -->
  <div class="abs center kicker" style="top:708px">ABOUT US</div>
  <h2 class="abs center heading" style="top:752px">WELCOME TO BRINDLE LANDSCAPES</h2>
  <svg class="abs swoosh" style="top:824px" viewBox="0 0 180 44"><path d="M0,42 C40,10 110,-2 180,12 C110,8 50,18 0,42 Z" fill="var(--green)"/></svg>
  <p class="abs center copy" style="top:882px;left:200px;width:800px">We at Brindle Landscapes are a professional, experienced landscaping business that delivers premium garden construction at an affordable price.</p>
  <p class="abs center copy" style="top:968px;left:160px;width:880px">We provide all aspects of hard and soft landscaping throughout Surrey and surrounding areas. We pride ourselves on excellent workmanship and attention to detail. Using only top quality materials to ensure an outstanding and long-lasting finish, installed using both traditional and modern techniques.</p>
  <div class="abs center call" style="top:1092px">Please call now for a free estimate</div>
  <div class="abs center phone-big" style="top:1128px">
    <svg viewBox="0 0 24 24"><path d="M6.6 10.8a15.2 15.2 0 0 0 6.6 6.6l2.2-2.2a1 1 0 0 1 1-.25 11.4 11.4 0 0 0 3.6.57 1 1 0 0 1 1 1V20a1 1 0 0 1-1 1A17 17 0 0 1 3 4a1 1 0 0 1 1-1h3.5a1 1 0 0 1 1 1c0 1.25.2 2.45.57 3.57a1 1 0 0 1-.25 1z"/></svg>
    07700 900 418
  </div>

  <!-- services -->
  <svg class="abs" style="left:0;top:1200px" width="1200" height="1070" viewBox="0 1200 1200 1070">
    <path d="M0,1480 C40,1290 280,1226 640,1220 C900,1216 1080,1236 1200,1270 L1200,2130 C1000,2210 720,2262 480,2246 C280,2232 100,2200 0,2186 Z" fill="var(--mist)"/>
  </svg>
  <div class="abs center kicker" style="top:1290px">WHAT WE DO</div>
  <h2 class="abs center heading" style="top:1334px">SERVICES</h2>
  <svg class="abs swoosh" style="top:1410px" viewBox="0 0 180 44"><path d="M0,42 C40,10 110,-2 180,12 C110,8 50,18 0,42 Z" fill="var(--green)"/></svg>
  <svg class="abs side-arrow" style="left:40px;top:1642px" viewBox="0 0 26 40"><path d="M20 4 L6 20 L20 36"/></svg>
  <svg class="abs side-arrow" style="left:1136px;top:1642px" viewBox="0 0 26 40"><path d="M6 4 L20 20 L6 36"/></svg>

  <div class="abs svc" style="left:104px;top:1475px">
    <div class="svc-ring"><div class="svc-photo" role="img" aria-label="Photo of a grey block paved driveway with drainage channel" style="background:linear-gradient(160deg,#9a8e82,#8d8f92 45%,#6a7d4a)"></div></div>
    <div class="svc-stem"></div>
  </div>
  <div class="abs svc" style="left:436px;top:1475px">
    <div class="svc-ring orange"><div class="svc-photo" role="img" aria-label="Photo of a brindle brick paved front drive" style="background:linear-gradient(160deg,#c9c6c0,#a08874 45%,#8c7a6a)"></div></div>
    <div class="svc-stem"></div>
  </div>
  <div class="abs svc" style="left:765px;top:1475px">
    <div class="svc-ring"><div class="svc-photo" role="img" aria-label="Photo of a new timber close board fence beside a lawn" style="background:linear-gradient(180deg,#8fb5e0,#b7a274 45%,#5d8a34)"></div></div>
    <div class="svc-stem"></div>
  </div>
  <svg class="abs" style="left:180px;top:1866px" width="180" height="44" viewBox="0 0 180 44"><path d="M0,42 C40,10 110,-2 180,12 C110,8 50,18 0,42 Z" fill="var(--green)"/></svg>
  <svg class="abs" style="left:512px;top:1866px" width="180" height="44" viewBox="0 0 180 44"><path d="M0,42 C40,10 110,-2 180,12 C110,8 50,18 0,42 Z" fill="var(--orange)"/></svg>
  <svg class="abs" style="left:841px;top:1866px" width="180" height="44" viewBox="0 0 180 44"><path d="M0,42 C40,10 110,-2 180,12 C110,8 50,18 0,42 Z" fill="var(--green)"/></svg>
  <div class="abs svc" style="left:104px;top:1870px"><div class="svc-title">DRIVEWAYS</div><p class="svc-text">We pride ourselves on excellent<br>workmanship &amp; attention to detail</p><a class="svc-more">READ MORE</a></div>
  <div class="abs svc" style="left:436px;top:1870px"><div class="svc-title">PAVING &amp; BRICKWORK</div><p class="svc-text">We pride ourselves on excellent<br>workmanship &amp; attention to detail</p><a class="svc-more orange">READ MORE</a></div>
  <div class="abs svc" style="left:765px;top:1870px"><div class="svc-title">FENCING &amp; DECKING</div><p class="svc-text">We pride ourselves on excellent<br>workmanship &amp; attention to detail</p><a class="svc-more">READ MORE</a></div>

  <!-- projects -->
  <div class="abs center kicker" style="top:2302px">GALLERY</div>
  <h2 class="abs center heading" style="top:2346px">PROJECTS</h2>
  <svg class="abs swoosh" style="top:2422px" viewBox="0 0 180 44"><path d="M0,42 C40,10 110,-2 180,12 C110,8 50,18 0,42 Z" fill="var(--green)"/></svg>

  <div class="abs tile" style="left:110px;top:2486px;width:311px;height:353px">
    <div class="tile-photo" role="img" aria-label="Photo of a garden lawn before fencing" style="height:164px;background:linear-gradient(180deg,#5d6e48,#6c8a3c)"></div>
    <div class="tile-photo" role="img" aria-label="Photo of the new timber fence after installation" style="height:164px;margin-top:8px;background:linear-gradient(180deg,#c7a36a,#9b7a44 70%,#5a4632)"></div>
  </div>
  <div class="abs tile" style="left:444px;top:2486px;width:310px;height:353px">
    <div class="tile-photo" role="img" aria-label="Photo of a swimming pool surrounded by sandstone paving" style="height:100%;background:linear-gradient(180deg,#6b5f4a 0%,#3fa6d9 30%,#4bb9e8 45%,#c7a686 60%,#b49476 100%)"></div>
  </div>
  <div class="abs tile" style="left:775px;top:2486px;width:312px;height:353px">
    <div class="tile-photo" role="img" aria-label="Photo of a garden being cleared before turfing" style="height:164px;background:linear-gradient(180deg,#5a6e44,#7a6a4e)"></div>
    <div class="tile-photo" role="img" aria-label="Photo of the same garden with fresh lawn laid" style="height:164px;margin-top:8px;background:linear-gradient(180deg,#5f7c3c,#5fa332)"></div>
  </div>
  <div class="abs tile" style="left:110px;top:2862px;width:471px;height:268px">
    <div class="tile-photo" role="img" aria-label="Photo of raised sleeper steps with artificial grass and grey paving" style="height:100%;background:linear-gradient(170deg,#4a3a30,#6f5a44 40%,#6aa93e 70%,#b9b3a8)"></div>
  </div>
  <div class="abs tile" style="left:610px;top:2862px;width:477px;height:268px">
    <div class="tile-photo" role="img" aria-label="Photo of a curved block paving path beside gravel" style="height:100%;background:linear-gradient(110deg,#d4d2ce,#b5b3b0 45%,#6c6c6e 75%,#4a4a4c)"></div>
  </div>
  <div class="abs btn" style="left:510px;top:3174px;width:180px;height:62px">VIEW MORE</div>

  <!-- testimonials -->
  <svg class="abs" style="left:0;top:3280px" width="1200" height="720" viewBox="0 3280 1200 720">
    <defs><linearGradient id="lawn" x1="0" y1="0" x2="1" y2="1"><stop offset="0" stop-color="#3f8a20"/><stop offset=".5" stop-color="#5aa534"/><stop offset="1" stop-color="#86c45c"/></linearGradient></defs>
    <path d="M0,3520 C280,3380 640,3282 1200,3320 L1200,3700 C1010,3880 640,3990 300,3970 C180,3962 80,3945 0,3930 Z" fill="url(#lawn)" role="img" aria-label="Green tinted photo of a paved patio with artificial lawn"/>
  </svg>
  <div class="abs quote-mark">&ldquo;</div>
  <div class="abs center kicker" style="top:3364px;color:var(--white)">REVIEWS</div>
  <h2 class="abs center heading light" style="top:3408px">CLIENT TESTIMONIALS</h2>
  <svg class="abs swoosh" style="top:3480px" viewBox="0 0 180 44"><path d="M0,42 C40,10 110,-2 180,12 C110,8 50,18 0,42 Z" fill="var(--white)"/></svg>
  <div class="abs avatar" role="img" aria-label="Client portrait"></div>
  <p class="abs review">Lorem ipsum dolor sit amet, consectetur adipiscing elit, sed do eiusmod tempor incidi dunt ut labore et dolore magna aliqua. Quis ipsum suspendisse ultrices gravida. Risus com modo viverra maecenas accumsan lacus vel facilisis.</p>
  <div class="abs center reviewer">- ALEX CARTER</div>
  <div class="abs round-btn" style="left:550px;top:3846px"><svg viewBox="0 0 18 18"><path d="M12 2 L5 9 L12 16"/></svg></div>
  <div class="abs round-btn" style="left:602px;top:3846px"><svg viewBox="0 0 18 18"><path d="M6 2 L13 9 L6 16"/></svg></div>

  <!-- contact -->
  <div class="abs center kicker" style="top:4030px">GET IN TOUCH</div>
  <h2 class="abs center heading" style="top:4074px">CONTACT US</h2>
  <svg class="abs swoosh" style="top:4146px" viewBox="0 0 180 44"><path d="M0,42 C40,10 110,-2 180,12 C110,8 50,18 0,42 Z" fill="var(--green)"/></svg>
  <div class="abs field" style="left:296px;top:4221px;width:307px;height:49px">Name</div>
  <div class="abs field" style="left:610px;top:4221px;width:307px;height:49px">Email</div>
  <div class="abs field" style="left:296px;top:4283px;width:307px;height:49px">Phone No</div>
  <div class="abs field" style="left:610px;top:4283px;width:307px;height:49px">Subject</div>
  <div class="abs field" style="left:296px;top:4343px;width:621px;height:91px">Message</div>
  <div class="abs btn" style="left:514px;top:4471px;width:172px;height:66px">SUBMIT</div>

  <!-- footer -->
  <svg class="abs" style="left:0;top:4570px" width="1200" height="422" viewBox="0 4570 1200 422">
    <path d="M0,4660 C360,4570 820,4570 1200,4640 L1200,4992 L0,4992 Z" fill="var(--green)"/>
    <path d="M0,4680 C360,4596 820,4596 1200,4664 L1200,4992 L0,4992 Z" fill="var(--ink)"/>
  </svg>
  <div class="abs center foot-brand">BRINDLE<div style="font-size:20px;letter-spacing:4px;margin-top:6px">LANDSCAPES</div></div>
  <div class="abs center foot-contact">
    <svg viewBox="0 0 24 24"><path d="M6.6 10.8a15.2 15.2 0 0 0 6.6 6.6l2.2-2.2a1 1 0 0 1 1-.25 11.4 11.4 0 0 0 3.6.57 1 1 0 0 1 1 1V20a1 1 0 0 1-1 1A17 17 0 0 1 3 4a1 1 0 0 1 1-1h3.5a1 1 0 0 1 1 1c0 1.25.2 2.45.57 3.57a1 1 0 0 1-.25 1z"/></svg>
    <span>07700 900 418</span><span>|</span>
    <svg viewBox="0 0 24 24"><path d="M2 5h20v14H2z"/></svg>
    <span>info@brindle-landscapes.com</span><span>|</span>
    <svg viewBox="0 0 24 24"><circle cx="12" cy="12" r="10"/></svg>
    <span>www.brindle-landscapes.com</span>
  </div>
  <div class="abs center socials"><span></span><span></span><span></span></div>
  <div class="abs center copyright">Copyright © 2020, Brindle Landscapes. All rights reserved.</div>

</div>
</body>
</html>
```